Interior designer needs a power point template design

I need a template PowerPoint design for my client presentations. The presentations I prepare for my clients usually include the furniture project, the detail of the selected furniture, and the costs. There are a lot of images I insert. What I need is to have a template that I can use for all my presentations, where from time to time I will insert the specific images and descriptions I want to insert. What will always be the same will be the cover, the colors, the font, and the design of the internal sections.
I already have my logo that I would like to insert on each page of the presentation (in small size).
In summary, I need:
- basic template design
- cover with an image chosen by Picsmeadow photo
- design an internal section/chapter
- internal page design.

I like the clolors of pink and brown <8please see image attached)
Images (will come from Picsmeadow photo)
● entrance/hall
● living room
● dining room
● Bathroom
● Closet
● Kids room
● Master bedroom
● Master bathroom
● Kitchen
● Office
● Laundry
● Balcony or Terrace

Target Market(s)

Customers (both residential and commercial projects)

Industry/Entity Type

interior design

Font styles to use
Other font styles liked:
• I like courier new

Requirements
Must have
• beautiful design
Should not have
• animations

```html
<!DOCTYPE html>
<html lang="en">
<head>
<meta charset="utf-8">
<title>Casa Lumina – Presentation Template</title>
<link rel="stylesheet" href="https://fonts.googleapis.com/css2?family=Oswald:wght@200;300&family=Montserrat:wght@400;500&display=swap">
<style>
  :root{
    --board:#414042;
    --white:#ffffff;
    --panel:#e2e2e2;
    --ink:#3c3c3c;
    --muted:#6d6d6d;
    --coral:#e88f80;
    --terracotta:#d9764d;
    --blush:#e99489;
    --pale:#f6cbbd;
    --footer-grey:#ebebeb;
    --line:#d4d4d4;
  }
  *{box-sizing:border-box;margin:0;padding:0}
  html,body{width:1200px;height:2476px;overflow:hidden}
  body{background:var(--board);position:relative;font-family:"Montserrat",sans-serif;color:var(--ink)}

  .slide{position:absolute;width:540px;height:303px;overflow:hidden;background:var(--white)}
  .slide--hero{left:159px;top:84px;transform:scale(1.6333);transform-origin:0 0}
  .slide--warm{background:linear-gradient(90deg,var(--terracotta) 0%,var(--blush) 100%)}
  .slide--split{background:linear-gradient(90deg,var(--panel) 0 50%,var(--white) 50% 100%)}
  .slide--split-rev{background:linear-gradient(90deg,var(--white) 0 50%,var(--panel) 50% 100%)}
  .slide--top{background:linear-gradient(180deg,var(--panel) 0 150px,var(--white) 150px 100%)}
  .slide--kids{background:linear-gradient(180deg,var(--panel) 0 185px,var(--white) 185px 100%)}

  .display{font-family:"Oswald",sans-serif;font-weight:200;text-transform:uppercase;letter-spacing:.5px;line-height:1}

  /* brand name block */
  .brand{position:absolute;display:flex;flex-direction:column;align-items:center;color:var(--ink)}
  .brand svg{display:block}
  .brand__name{font-family:"Oswald",sans-serif;font-weight:200;text-transform:uppercase;letter-spacing:2px;line-height:1;text-align:center;margin-top:6px}
  .slide--warm .brand{color:var(--pale)}

  /* cover */
  .cover__rule-v{position:absolute;left:188px;top:50px;width:1px;height:190px;background:var(--line)}
  .cover__rule-h{position:absolute;left:170px;top:146px;width:330px;height:1px;background:var(--line)}
  .slide--warm .cover__rule-v,.slide--warm .cover__rule-h{background:rgba(255,255,255,.25)}
  .cover__kicker{position:absolute;left:227px;top:77px;font-size:19px;color:var(--ink)}
  .cover__title{position:absolute;left:227px;top:105px;font-size:34px;color:var(--ink)}
  .cover__sub{position:absolute;left:227px;top:157px;font-size:11.5px;font-weight:300;color:var(--ink)}
  .cover__date{position:absolute;left:228px;top:188px;width:121px;height:17px;background:var(--coral);color:#f9d4cc;font-family:"Oswald",sans-serif;font-weight:200;font-size:8px;letter-spacing:1px;display:flex;align-items:center;justify-content:center;border-radius:2px}
  .slide--warm .cover__kicker,.slide--warm .cover__title,.slide--warm .cover__sub{color:var(--pale)}
  .slide--warm .cover__date{background:rgba(255,255,255,.15);color:var(--pale)}

  .footer-band{position:absolute;left:0;bottom:0;width:100%;height:18px;background:var(--coral);color:var(--white);font-size:6.5px;letter-spacing:.4px;display:flex;align-items:center;justify-content:center}
  .slide--warm .footer-band{background:var(--footer-grey);color:var(--muted)}

  /* internal pages */
  .page-bar{position:absolute;left:12px;right:0;top:278px;height:7px;border-radius:4px 0 0 4px;background:linear-gradient(90deg,var(--terracotta),var(--blush));color:var(--white);font-size:3.6px;display:flex;align-items:center;justify-content:space-between;padding:0 10px 0 6px}
  .photo{position:absolute;border:2px solid var(--white);box-shadow:0 0 0 .5px #c9c9c9}
  .section-title{position:absolute;font-size:25px;color:var(--ink)}
  .section-text{position:absolute;font-size:6.3px;line-height:1.25;color:var(--ink)}
  .center{text-align:center;transform:translateX(-50%)}
  .divider{position:absolute;width:.5px;background:#bdbdbd}

  /* closing */
  .contact__kicker{position:absolute;left:227px;top:80px;font-size:18px;color:var(--pale)}
  .contact__name{position:absolute;left:227px;top:103px;font-size:31px;color:var(--pale)}
  .contact__address{position:absolute;left:227px;top:158px;font-family:"Oswald",sans-serif;font-weight:200;font-size:10px;color:var(--pale);text-transform:uppercase}
  .contact__list{position:absolute;left:227px;top:181px;list-style:none;color:var(--pale);font-size:6.5px}
  .contact__list li{display:flex;align-items:center;gap:7px;height:15px}
  .contact__list svg{width:9px;height:9px}
</style>
</head>
<body>

<!-- Hero cover -->
<section class="slide slide--hero">
  <div class="brand" style="left:60px;top:80px">
    <svg width="80" height="80" viewBox="0 0 80 80"><circle cx="40" cy="40" r="38" fill="none" stroke="currentColor" stroke-width="1"/></svg>
    <span class="brand__name" style="font-size:16px">Casa Lumina</span>
  </div>
  <div class="cover__rule-v"></div><div class="cover__rule-h"></div>
  <p class="cover__kicker display">Casa Lumina</p>
  <h1 class="cover__title display">Presentation Title</h1>
  <p class="cover__sub display">Subtitle of presentation goes here!</p>
  <p class="cover__date">FRIDAY, APRIL 15, 2022</p>
  <footer class="footer-band">© 2022 CASA LUMINA, All rights reserved.</footer>
</section>

<!-- Cover light -->
<section class="slide" style="left:51px;top:836px">
  <div class="brand" style="left:60px;top:80px">
    <svg width="80" height="80" viewBox="0 0 80 80"><circle cx="40" cy="40" r="38" fill="none" stroke="currentColor" stroke-width="1"/></svg>
    <span class="brand__name" style="font-size:16px">Casa Lumina</span>
  </div>
  <div class="cover__rule-v"></div><div class="cover__rule-h"></div>
  <p class="cover__kicker display">Casa Lumina</p>
  <h2 class="cover__title display">Presentation Title</h2>
  <p class="cover__sub display">Subtitle of presentation goes here!</p>
  <p class="cover__date">FRIDAY, APRIL 15, 2022</p>
  <footer class="footer-band">© 2022 CASA LUMINA, All rights reserved.</footer>
</section>

<!-- Cover warm -->
<section class="slide slide--warm" style="left:610px;top:836px">
  <div class="brand" style="left:60px;top:80px">
    <svg width="80" height="80" viewBox="0 0 80 80"><circle cx="40" cy="40" r="38" fill="none" stroke="currentColor" stroke-width="1"/></svg>
    <span class="brand__name" style="font-size:16px">Casa Lumina</span>
  </div>
  <div class="cover__rule-v"></div><div class="cover__rule-h"></div>
  <p class="cover__kicker display">Casa Lumina</p>
  <h2 class="cover__title display">Presentation Title</h2>
  <p class="cover__sub display">Subtitle of presentation goes here!</p>
  <p class="cover__date">FRIDAY, APRIL 15, 2022</p>
  <footer class="footer-band">© 2022 CASA LUMINA, All rights reserved.</footer>
</section>

<!-- Bedroom -->
<section class="slide slide--split" style="left:51px;top:1159px">
  <div class="brand" style="left:90px;top:58px">
    <svg width="44" height="44" viewBox="0 0 44 44"><circle cx="22" cy="22" r="21" fill="none" stroke="currentColor" stroke-width=".8"/></svg>
    <span class="brand__name" style="font-size:9px">Casa Lumina</span>
  </div>
  <h3 class="section-title display center" style="left:112px;top:165px">Bedroom</h3>
  <p class="section-text center" style="left:112px;top:200px;width:180px">Lorem ipsum dolor sit amet, consectetur adipiscing elit. Vivamus eu dui ex.</p>
  <div class="photo" role="img" aria-label="Bright master bedroom with beamed ceiling and neutral bedding" style="left:225px;top:12px;width:302px;height:251px;background:linear-gradient(160deg,#ece7e0 0%,#cfc5b8 55%,#8f877e 100%)"></div>
  <div class="page-bar"><span>© 2022 CASA LUMINA, All rights reserved.</span><span>3</span></div>
</section>

<!-- Bathroom -->
<section class="slide slide--split-rev" style="left:610px;top:1159px">
  <div class="photo" role="img" aria-label="White bathroom with freestanding tub and wooden floor" style="left:13px;top:12px;width:302px;height:251px;background:linear-gradient(180deg,#f2f2f0 0%,#e3e1dc 60%,#c9a684 100%)"></div>
  <div class="brand" style="left:408px;top:58px">
    <svg width="44" height="44" viewBox="0 0 44 44"><circle cx="22" cy="22" r="21" fill="none" stroke="currentColor" stroke-width=".8"/></svg>
    <span class="brand__name" style="font-size:9px">Casa Lumina</span>
  </div>
  <h3 class="section-title display center" style="left:430px;top:165px">Bathroom</h3>
  <p class="section-text center" style="left:430px;top:200px;width:180px">Lorem ipsum dolor sit amet, consectetur adipiscing elit. Vivamus eu dui ex.</p>
  <div class="page-bar"><span>© 2022 CASA LUMINA, All rights reserved.</span><span>4</span></div>
</section>

<!-- Dining room -->
<section class="slide slide--top" style="left:51px;top:1481px">
  <div class="brand" style="left:36px;top:36px">
    <svg width="40" height="40" viewBox="0 0 44 44"><circle cx="22" cy="22" r="21" fill="none" stroke="currentColor" stroke-width=".8"/></svg>
    <span class="brand__name" style="font-size:8px">Casa Lumina</span>
  </div>
  <div class="divider" style="left:102px;top:44px;height:56px"></div>
  <h3 class="section-title display" style="left:123px;top:46px">Dining Room</h3>
  <p class="section-text" style="left:123px;top:83px;width:390px">Lorem ipsum dolor sit amet, consectetur adipiscing elit. Vivamus eu dui ex. Curabitur dapibus dignissim dui, in molestie metus feugiat sed. Praesent aliquet lorem ex, eu dapibus odio varius.</p>
  <div class="photo" role="img" aria-label="Dining table by large windows with garden view" style="left:12px;top:163px;width:254px;height:100px;background:linear-gradient(90deg,#e9e7e2 0%,#b9c6a6 60%,#5f7a4a 100%)"></div>
  <div class="photo" role="img" aria-label="Dining area with grey wall and white shelving" style="left:275px;top:163px;width:254px;height:100px;background:linear-gradient(90deg,#6e7479 0%,#8d8c86 55%,#e7e3dc 100%)"></div>
  <div class="page-bar"><span>© 2022 CASA LUMINA, All rights reserved.</span><span>5</span></div>
</section>

<!-- Kitchen -->
<section class="slide slide--split" style="left:610px;top:1481px">
  <div class="brand" style="left:90px;top:60px">
    <svg width="44" height="44" viewBox="0 0 44 44"><circle cx="22" cy="22" r="21" fill="none" stroke="currentColor" stroke-width=".8"/></svg>
    <span class="brand__name" style="font-size:9px">Casa Lumina</span>
  </div>
  <h3 class="section-title display center" style="left:112px;top:165px">Kitchen</h3>
  <p class="section-text center" style="left:112px;top:200px;width:180px">Lorem ipsum dolor sit amet, consectetur adipiscing elit. Vivamus eu dui ex.</p>
  <div class="photo" role="img" aria-label="Light kitchen with pendant lamps and breakfast bar" style="left:224px;top:13px;width:303px;height:120px;background:linear-gradient(180deg,#e5e6e4 0%,#d6d2ca 60%,#c19a6f 100%)"></div>
  <div class="photo" role="img" aria-label="Modern kitchen with white cabinets and wooden island" style="left:224px;top:144px;width:303px;height:120px;background:linear-gradient(90deg,#e9e6e1 0%,#c9ab86 55%,#4a3e37 100%)"></div>
  <div class="page-bar"><span>© 2022 CASA LUMINA, All rights reserved.</span><span>6</span></div>
</section>

<!-- Balcony -->
<section class="slide slide--split-rev" style="left:51px;top:1803px">
  <div class="photo" role="img" aria-label="Terrace lounge with white sofa and tall grasses" style="left:13px;top:13px;width:303px;height:120px;background:linear-gradient(90deg,#e9e7e3 0%,#8d7e6c 55%,#c4a25e 100%)"></div>
  <div class="photo" role="img" aria-label="Balcony living area with yellow sofa and floor lamp" style="left:13px;top:144px;width:303px;height:120px;background:linear-gradient(90deg,#e7e7e5 0%,#3d4550 45%,#e0b72f 75%,#ece9e2 100%)"></div>
  <div class="brand" style="left:408px;top:60px">
    <svg width="44" height="44" viewBox="0 0 44 44"><circle cx="22" cy="22" r="21" fill="none" stroke="currentColor" stroke-width=".8"/></svg>
    <span class="brand__name" style="font-size:9px">Casa Lumina</span>
  </div>
  <h3 class="section-title display center" style="left:430px;top:165px">Balcony</h3>
  <p class="section-text center" style="left:430px;top:200px;width:180px">Lorem ipsum dolor sit amet, consectetur adipiscing elit. Vivamus eu dui ex.</p>
  <div class="page-bar"><span>© 2022 CASA LUMINA, All rights reserved.</span><span>7</span></div>
</section>

<!-- Kids room -->
<section class="slide slide--kids" style="left:610px;top:1803px">
  <div class="brand" style="left:42px;top:42px">
    <svg width="42" height="42" viewBox="0 0 44 44"><circle cx="22" cy="22" r="21" fill="none" stroke="currentColor" stroke-width=".8"/></svg>
    <span class="brand__name" style="font-size:8px">Casa Lumina</span>
  </div>
  <div class="divider" style="left:112px;top:48px;height:60px"></div>
  <h3 class="section-title display" style="left:129px;top:50px">Kids Room</h3>
  <p class="section-text" style="left:129px;top:87px;width:390px">Lorem ipsum dolor sit amet, consectetur adipiscing elit. Vivamus eu dui ex. Curabitur dapibus dignissim dui, in molestie metus feugiat sed. Praesent aliquet lorem ex, eu dapibus odio varius.</p>
  <div class="photo" role="img" aria-label="Children's room with teal wall and small furniture" style="left:19px;top:128px;width:164px;height:113px;background:linear-gradient(180deg,#7fa9a3 0%,#8fb0a9 60%,#a98a6e 100%)"></div>
  <div class="photo" role="img" aria-label="Bright nursery with white furniture and wall art" style="left:189px;top:128px;width:162px;height:113px;background:linear-gradient(180deg,#f1efec 0%,#e6e0d7 65%,#c9b89f 100%)"></div>
  <div class="photo" role="img" aria-label="Playroom with colourful shelves and pink rug" style="left:358px;top:128px;width:163px;height:113px;background:linear-gradient(160deg,#f0ede8 0%,#d9d1c4 55%,#e26d9a 100%)"></div>
  <div class="page-bar"><span>© 2022 CASA LUMINA, All rights reserved.</span><span>8</span></div>
</section>

<!-- Closing / contacts -->
<section class="slide slide--warm" style="left:330px;top:2124px">
  <div class="brand" style="left:62px;top:80px">
    <svg width="80" height="80" viewBox="0 0 80 80"><circle cx="40" cy="40" r="38" fill="none" stroke="currentColor" stroke-width="1"/></svg>
    <span class="brand__name" style="font-size:16px">Casa Lumina</span>
  </div>
  <div class="cover__rule-v"></div>
  <p class="contact__kicker display">Casa</p>
  <h2 class="contact__name display">Lumina</h2>
  <p class="contact__address">di Marta Venturi, Via dei Ciliegi, 24</p>
  <ul class="contact__list">
    <li><svg viewBox="0 0 24 24"><path d="M6.6 10.8a15 15 0 0 0 6.6 6.6l2.2-2.2a1 1 0 0 1 1-.25 11.4 11.4 0 0 0 3.6.57 1 1 0 0 1 1 1V20a1 1 0 0 1-1 1A17 17 0 0 1 3 4a1 1 0 0 1 1-1h3.5a1 1 0 0 1 1 1c0 1.25.2 2.45.57 3.57a1 1 0 0 1-.25 1z" fill="currentColor"/></svg>340/5551872</li>
    <li><svg viewBox="0 0 24 24"><circle cx="12" cy="12" r="4" fill="none" stroke="currentColor" stroke-width="2.4"/><path d="M16 8v5a3 3 0 0 0 6 0v-1a10 10 0 1 0-4 8" fill="none" stroke="currentColor" stroke-width="2.4"/></svg>martaventuri@mailbox.com</li>
    <li><svg viewBox="0 0 24 24" fill="none" stroke="currentColor" stroke-width="1.8"><circle cx="12" cy="12" r="10"/><path d="M2 12h20M12 2c3 3 3 17 0 20M12 2c-3 3-3 17 0 20"/></svg>www.martaventuri.com</li>
  </ul>
  <footer class="footer-band">© 2022 CASA LUMINA, All rights reserved.</footer>
</section>

</body>
</html>
```